Thank you for shopping with us business card

We would like a thank you card for our rebranded business. We used to be "Brindle Goods" but are now "Marlow Finds. Old thank you card and new logo will be attached for reference. New thank you card does not have to be same design as old thank you card, but please use new logo.
Shopmart URL is now marlowfinds.shopmart.example
Instagram is @Marlow_Finds
Email is marlowfinds@mailbox.example
Thank you!

Contact Information for Business Card

Shopmart site, email, Instagram

```html
<!DOCTYPE html>
<html lang="en">
<head>
<meta charset="utf-8">
<title>Marlow Finds – Thank You Card</title>
<link rel="stylesheet" href="https://fonts.googleapis.com/css2?family=Alfa+Slab+One&family=Didact+Gothic&family=Montserrat:wght@600;800&display=swap">
<style>
  :root {
    --navy: #33304f;
    --cyan: #47c3e6;
    --white: #ffffff;
    --stage: #2a2c30;
  }
  * { box-sizing: border-box; margin: 0; padding: 0; }
  html, body { width: 1200px; height: 780px; overflow: hidden; }
  body {
    background: var(--stage);
    display: flex;
    align-items: center;
    justify-content: center;
    gap: 40px;
  }
  .card {
    position: relative;
    width: 540px;
    height: 309px;
    border-radius: 22px;
    overflow: hidden;
  }

  /* Front: brand and contacts */
  .card--front {
    background: var(--navy);
    color: var(--white);
    padding: 44px 40px 30px;
    display: flex;
    flex-direction: column;
    justify-content: space-between;
  }
  .brand {
    display: flex;
    align-items: center;
    gap: 20px;
    padding-left: 40px;
  }
  .brand__dot {
    width: 62px;
    height: 62px;
    border-radius: 50%;
    background: var(--white);
    flex: none;
  }
  .brand__name {
    font-family: "Montserrat", sans-serif;
    font-weight: 600;
    font-size: 44px;
    line-height: 1.02;
    letter-spacing: 1px;
    text-transform: uppercase;
  }
  .contacts {
    list-style: none;
    font-family: "Didact Gothic", sans-serif;
    font-size: 16px;
    display: grid;
    gap: 8px;
  }
  .contacts__item { display: flex; align-items: center; gap: 10px; }
  .contacts__icon {
    width: 14px; height: 14px; border-radius: 50%;
    background: var(--cyan); flex: none;
  }

  /* Back: thank you note */
  .card--back {
    background: var(--cyan);
    color: var(--navy);
  }
  .thanks {
    position: absolute;
    left: 30px; top: 26px;
    display: flex;
    gap: 18px;
  }
  .thanks__big {
    font-family: "Alfa Slab One", serif;
    color: var(--white);
    font-size: 54px;
    line-height: 0.95;
    text-transform: uppercase;
  }
  .thanks__big span { display: block; }
  .thanks__big span + span { padding-left: 40px; }
  .thanks__side { padding-top: 4px; }
  .thanks__sub {
    font-family: "Montserrat", sans-serif;
    font-weight: 800;
    font-size: 22px;
    line-height: 1.05;
    text-transform: uppercase;
  }
  .thanks__rule {
    width: 300px; height: 3px;
    background: var(--navy);
    margin: 10px 0 8px;
  }
  .thanks__note {
    font-family: "Didact Gothic", sans-serif;
    font-size: 16px;
    line-height: 1.2;
    max-width: 230px;
  }
  .signoff {
    position: absolute;
    right: 34px; top: 150px;
    font-family: "Montserrat", sans-serif;
    font-weight: 800;
    font-size: 15px;
    text-transform: uppercase;
    letter-spacing: 0.5px;
  }
  .review {
    position: absolute;
    left: 0; right: 0; bottom: 0;
    height: 92px;
    background: var(--navy);
    color: var(--white);
    text-align: center;
    padding-top: 20px;
  }
  .review::before {
    content: "";
    position: absolute;
    left: 0; right: 0; top: 7px;
    height: 2px;
    background: var(--cyan);
  }
  .review__stars { font-size: 14px; letter-spacing: 8px; }
  .review__text {
    font-family: "Didact Gothic", sans-serif;
    font-size: 22px;
    margin-top: 4px;
  }
</style>
</head>
<body>
  <section class="card card--front" aria-label="Business card front">
    <div class="brand">
      <span class="brand__dot"></span>
      <h1 class="brand__name">Marlow<br>Finds</h1>
    </div>
    <ul class="contacts">
      <li class="contacts__item"><span class="contacts__icon"></span>marlowfinds.shopmart.example</li>
      <li class="contacts__item"><span class="contacts__icon"></span>@Marlow_Finds</li>
      <li class="contacts__item"><span class="contacts__icon"></span>marlowfinds@mailbox.example</li>
    </ul>
  </section>

  <section class="card card--back" aria-label="Business card back">
    <div class="thanks">
      <h2 class="thanks__big"><span>Thank</span><span>You</span></h2>
      <div class="thanks__side">
        <p class="thanks__sub">For<br>your purchase</p>
        <div class="thanks__rule"></div>
        <p class="thanks__note">Your purchase made my day and I hope this package brightens yours.</p>
      </div>
    </div>
    <p class="signoff">Marlow Finds</p>
    <div class="review">
      <div class="review__stars" aria-label="Five stars">★★★★★</div>
      <p class="review__text">please come back and leave a review</p>
    </div>
  </section>
</body>
</html>
```